Letterhead Design Project

I need a simple, clean and corporate letterhead & follow-on letterhead.
The follow-on letterhead should just have the logo only.
Final File Specs:
Full Bleed Size (starting document size)
213 x 300 mm
2517 x 3544 pixels
* Finished artwork should use the full bleed dimensions for best results.
Document Trim Size (final size after being cut)
210 x 297 mm
2480 x 3508 pixels
* Please be sure to keep all text within the safe margin.
Resolution 300 DPI
Accepted file types:-
Adobe Acrobat 9 Document (*.pdf) (recommended)
Adobe Illustrator CS3 Artwork (*.ai) (recommended)
Adobe Photoshop CS3 Image (*.psd) (recommended)
Bitmap Image (*.bmp)
GIF Image (*.gif)
JPEG Image (*.jpg,*.jpeg)
Microsoft PowerPoint 2010 Document (*.ppt)
Microsoft Publisher 2010 Document (*.pub)
Microsoft Word 2010 Document (*.doc)
PCX Image (*.pcx)
PICT Image (*.pic,*.pict,*.pct)
PNG Image (*.png)
PostScript Document (*.ps)
TIF Image (*.tif,*.tiff)
Windows Enhanced Metafile (*.emf)
Windows Metafile (*.wmf)
Requirements
Must have
- My letterhead must have:-
- Logo
- ACN - 482 617 309
- address - Suite 8, 51 Hartwell Ave, Larkfield, NSW 2187
- phone - (02) 8371 5926
- fax - (02) 8352 6149
- email - info@brantorguard.com.au
- web - www.brantorguard.com.au
Follow-on letterhead should have the logo only

```html
<!DOCTYPE html>
<html lang="en">
<head>
<meta charset="utf-8">
<title>Brantor Guard Letterhead</title>
<link href="https://fonts.googleapis.com/css2?family=Open+Sans:wght@400;600;700&family=Great+Vibes&display=swap" rel="stylesheet">
<style>
  :root {
    --backdrop: #e4e4e4;
    --paper: #fbfbfb;
    --ink: #6a6a6a;
    --ink-strong: #555555;
    --navy: #2f3142;
    --lime: #9bc23c;
  }
  * { margin: 0; padding: 0; box-sizing: border-box; }
  html, body {
    width: 1200px; height: 800px; overflow: hidden;
    background: var(--backdrop);
    font-family: "Open Sans", sans-serif;
  }
  .canvas { position: relative; width: 1200px; height: 800px; }
  .sheet {
    position: absolute; top: 111px;
    width: 410px; height: 574px;
    background: var(--paper);
    box-shadow: 0 1px 3px rgba(0,0,0,0.08);
  }
  .sheet--first { left: 165px; }
  .sheet--follow { left: 613px; }

  .edge-bar {
    position: absolute; left: 0; top: 49px;
    width: 6px; height: 43px; background: var(--navy);
  }
  .contact {
    position: absolute; left: 27px; top: 49px;
    font-size: 5.6px; line-height: 7.5px; color: var(--navy);
    list-style: none;
  }
  .contact .key { color: var(--lime); margin-right: 3px; }

  .brand {
    position: absolute; display: flex; align-items: center;
    color: var(--navy); font-weight: 700; white-space: nowrap;
  }
  .brand .mark { background: var(--lime); flex: none; }
  .brand--header { right: 36px; top: 40px; font-size: 17px; gap: 6px; }
  .brand--header .mark { width: 14px; height: 14px; }
  .brand--footer { right: 30px; bottom: 46px; font-size: 12px; gap: 5px; }
  .brand--footer .mark { width: 10px; height: 10px; }

  .letter {
    position: absolute; left: 47px; width: 340px;
    font-size: 7.3px; line-height: 10.9px; color: var(--ink);
  }
  .sheet--first .letter { top: 148px; }
  .sheet--follow .letter { top: 145px; left: 49px; }
  .letter .greeting { font-weight: 700; color: var(--ink-strong); margin-bottom: 11px; }
  .letter p { margin-bottom: 11px; }
  .signoff { margin-top: 30px; }
  .signoff .signature {
    font-family: "Great Vibes", cursive;
    font-size: 22px; line-height: 22px; color: var(--ink-strong);
  }
  .signoff .role { font-weight: 700; color: var(--ink); font-size: 7.3px; margin-top: 0; }
</style>
</head>
<body>
<div class="canvas">

  <section class="sheet sheet--first">
    <div class="edge-bar"></div>
    <ul class="contact">
      <li><span class="key">P</span>(02) 8371 5926</li>
      <li><span class="key">F</span>(02) 8352 6149</li>
      <li><span class="key">E</span>info@brantorguard.com.au</li>
      <li>www.brantorguard.com.au</li>
      <li>Suite 8, 51 Hartwell Ave, Larkfield, NSW 2187</li>
      <li>ACN - 482 617 309</li>
    </ul>
    <div class="brand brand--header"><span class="mark"></span>Brantor Guard</div>

    <article class="letter">
      <div class="greeting">Lorem Ipsum,</div>
      <p>Cras mattis consectetur purus sit amet fermentum. Etiam porta sem malesuada magna mollis euismod. Integer posuere erat a ante venenatis dapibus posuere velit aliquet. Cras justo odio, dapibus ac facilisis in, egestas eget quam. Aenean eu leo quam. Pellentesque ornare sem lacinia quam venenatis vestibulum.</p>
      <p>Vivamus sagittis lacus vel augue laoreet rutrum faucibus dolor auctor. Donec sed odio dui. Etiam porta sem malesuada magna mollis euismod. Morbi leo risus, porta ac consectetur ac, vestibulum at eros. Nullam id dolor id nibh ultricies vehicula ut id elit.</p>
      <p>Donec id elit non mi porta gravida at eget metus. Fusce dapibus, tellus ac cursus commodo, tortor mauris condimentum nibh, ut fermentum massa justo sit amet risus. Cras justo odio, dapibus ac facilisis in, egestas eget quam. Cum sociis natoque penatibus et magnis dis parturient montes, nascetur ridiculus mus.</p>
      <p>Cum sociis natoque penatibus et magnis dis parturient montes, nascetur ridiculus mus. Curabitur blandit tempus porttitor. Aenean lacinia bibendum nulla sed consectetur. Lorem ipsum dolor sit amet, consectetur adipiscing elit.</p>
      <p>Cras justo odio, dapibus ac facilisis in, egestas eget quam. Morbi leo risus, porta ac consectetur ac, vestibulum at eros. Duis mollis, est non commodo luctus, nisi erat porttitor ligula, eget lacinia odio sem nec elit. Integer posuere erat a ante venenatis dapibus posuere velit aliquet. Vivamus sagittis lacus vel augue laoreet rutrum faucibus dolor auctor.</p>
      <div class="signoff">
        <div class="signature">Your Name</div>
        <div class="role">Company Director</div>
      </div>
    </article>
  </section>

  <section class="sheet sheet--follow">
    <article class="letter">
      <div class="greeting">Lorem Ipsum,</div>
      <p>Cras mattis consectetur purus sit amet fermentum. Etiam porta sem malesuada magna mollis euismod. Integer posuere erat a ante venenatis dapibus posuere velit aliquet. Cras justo odio, dapibus ac facilisis in, egestas eget quam. Aenean eu leo quam. Pellentesque ornare sem lacinia quam venenatis vestibulum.</p>
      <p>Vivamus sagittis lacus vel augue laoreet rutrum faucibus dolor auctor. Donec sed odio dui. Etiam porta sem malesuada magna mollis euismod. Morbi leo risus, porta ac consectetur ac, vestibulum at eros. Nullam id dolor id nibh ultricies vehicula ut id elit.</p>
      <p>Donec id elit non mi porta gravida at eget metus. Fusce dapibus, tellus ac cursus commodo, tortor mauris condimentum nibh, ut fermentum massa justo sit amet risus. Cras justo odio, dapibus ac facilisis in, egestas eget quam. Cum sociis natoque penatibus et magnis dis parturient montes, nascetur ridiculus mus.</p>
      <p>Cum sociis natoque penatibus et magnis dis parturient montes, nascetur ridiculus mus. Curabitur blandit tempus porttitor. Aenean lacinia bibendum nulla sed consectetur. Lorem ipsum dolor sit amet, consectetur adipiscing elit.</p>
      <p>Cras justo odio, dapibus ac facilisis in, egestas eget quam. Morbi leo risus, porta ac consectetur ac, vestibulum at eros. Duis mollis, est non commodo luctus, nisi erat porttitor ligula, eget lacinia odio sem nec elit. Integer posuere erat a ante venenatis dapibus posuere velit aliquet. Vivamus sagittis lacus vel augue laoreet rutrum faucibus dolor auctor.</p>
      <div class="signoff">
        <div class="signature">Your Name</div>
        <div class="role">Company Director</div>
      </div>
    </article>
    <div class="brand brand--footer"><span class="mark"></span>Brantor Guard</div>
  </section>

</div>
</body>
</html>
```